Corvane Tables business cards

I’d like a business card design that includes my logo, a tag line and my contact info. Black, textured background. My contact info color should match the orange and blue gradients. Tagline under logo: “Wooden Tables and Furniture of the Highest Quality”

Target Market(s)

High end furniture buyers

Contact Information for Business Card

Contact info, logo and tagline

```html
<!DOCTYPE html>
<html lang="en">
<head>
<meta charset="utf-8">
<title>Corvane Tables – Business Cards</title>
<link rel="stylesheet" href="https://fonts.googleapis.com/css2?family=Open+Sans:wght@400;600&family=Arimo:wght@400&display=swap">
<style>
  :root {
    --backdrop: #9a9a9a;
    --card: #252525;
    --card-edge: #1c1c1c;
    --orange: #e8661c;
    --orange-deep: #c9540f;
    --blue: #2f6fe0;
    --white: #f2f2f2;
    --divider: #8a8a8a;
  }
  * { box-sizing: border-box; margin: 0; padding: 0; }
  html, body { width: 1200px; height: 1050px; overflow: hidden; }
  body {
    background: var(--backdrop);
    font-family: "Arimo", Arial, sans-serif;
    position: relative;
  }
  .card {
    position: absolute;
    left: 180px;
    width: 840px;
    height: 480px;
    background: radial-gradient(ellipse at 30% 20%, #2c2c2c 0%, var(--card) 55%, var(--card-edge) 100%);
    border-bottom: 4px solid var(--orange-deep);
    box-shadow: 0 14px 30px rgba(0,0,0,0.28);
    overflow: hidden;
  }
  .card-texture { position: absolute; inset: 0; width: 100%; height: 100%; opacity: 0.35; }

  /* Front: contact side */
  .card--front { top: 30px; }
  .identity {
    position: absolute;
    top: 150px;
    right: 430px;
    text-align: right;
    color: var(--white);
    font-size: 21px;
    line-height: 29px;
  }
  .identity-name {
    font-family: "Open Sans", Arial, sans-serif;
    color: var(--orange);
    font-size: 31px;
    line-height: 40px;
    letter-spacing: 1px;
    margin-bottom: 2px;
  }
  .divider {
    position: absolute;
    left: 430px;
    top: 158px;
    width: 1px;
    height: 150px;
    background: var(--divider);
  }
  .contact-list {
    position: absolute;
    left: 452px;
    top: 166px;
    list-style: none;
    color: var(--white);
    font-size: 21px;
    line-height: 33px;
  }
  .contact-list li { display: flex; align-items: center; gap: 12px; }
  .contact-icon { width: 20px; height: 20px; flex: none; fill: var(--orange); }
  .tagline-band {
    position: absolute;
    left: 0; right: 0;
    top: 360px;
    height: 26px;
    background: var(--orange);
  }
  .tagline-strip {
    position: absolute;
    left: 0; right: 0;
    top: 394px;
    text-align: center;
    color: var(--white);
    font-size: 19px;
    letter-spacing: 4px;
    text-transform: uppercase;
  }
  .tagline-base {
    position: absolute;
    left: 0; right: 0;
    bottom: 0;
    height: 22px;
    background: var(--orange);
  }

  /* Back: brand side */
  .card--back { top: 540px; }
  .brand-name {
    position: absolute;
    left: 0; right: 0;
    top: 150px;
    text-align: center;
    font-family: "Open Sans", Arial, sans-serif;
    font-weight: 600;
    font-size: 76px;
    line-height: 1;
    color: var(--orange);
  }
  .brand-tagline {
    position: absolute;
    left: 0; right: 0;
    top: 268px;
    text-align: center;
    font-family: "Open Sans", Arial, sans-serif;
    font-size: 25px;
    letter-spacing: 1px;
    color: var(--blue);
  }
</style>
</head>
<body>
  <svg width="0" height="0" style="position:absolute">
    <defs>
      <filter id="paper-grain">
        <feTurbulence type="fractalNoise" baseFrequency="0.9" numOctaves="3" seed="4"/>
        <feColorMatrix values="0 0 0 0 0.5  0 0 0 0 0.5  0 0 0 0 0.5  0 0 0 0.45 0"/>
      </filter>
    </defs>
  </svg>

  <section class="card card--front">
    <svg class="card-texture" aria-hidden="true"><rect width="100%" height="100%" filter="url(#paper-grain)"/></svg>

    <div class="identity">
      <p class="identity-name">Marcus Ellery</p>
      <p>Managing Director</p>
      <p>4120 Alderwood Court</p>
      <p>Juneau, Alaska 99801</p>
    </div>

    <div class="divider"></div>

    <ul class="contact-list">
      <li>
        <svg class="contact-icon" viewBox="0 0 24 24" aria-hidden="true"><path d="M6.6 10.8a15.1 15.1 0 0 0 6.6 6.6l2.2-2.2c.3-.3.7-.4 1-.2 1.1.4 2.3.6 3.6.6.6 0 1 .4 1 1V20c0 .6-.4 1-1 1A17 17 0 0 1 3 4c0-.6.4-1 1-1h3.5c.6 0 1 .4 1 1 0 1.3.2 2.5.6 3.6.1.3 0 .7-.2 1z"/></svg>
        <span>555-201-4387</span>
      </li>
      <li>
        <svg class="contact-icon" viewBox="0 0 24 24" aria-hidden="true"><path d="M7 1h10a2 2 0 0 1 2 2v18a2 2 0 0 1-2 2H7a2 2 0 0 1-2-2V3a2 2 0 0 1 2-2zm0 3v14h10V4zm5 15.5a1.2 1.2 0 1 0 0 2.4 1.2 1.2 0 0 0 0-2.4z"/></svg>
        <span>555-318-9026</span>
      </li>
      <li>
        <svg class="contact-icon" viewBox="0 0 24 24" aria-hidden="true"><path d="M2 5h20v14H2zm2 2v.5l8 5 8-5V7zm0 2.8V17h16V9.8l-8 5z"/></svg>
        <span>info@CorvaneTables</span>
      </li>
      <li>
        <svg class="contact-icon" viewBox="0 0 24 24" aria-hidden="true"><path d="M12 2a10 10 0 1 0 0 20 10 10 0 0 0 0-20zm-1 17.9A8 8 0 0 1 4.1 10.9L9 15.8v1a2 2 0 0 0 2 2zm6.9-2.5a2 2 0 0 0-1.9-1.4h-1v-3a1 1 0 0 0-1-1H8v-2h2a1 1 0 0 0 1-1V7h2a2 2 0 0 0 2-2v-.4a8 8 0 0 1 2.9 12.8z"/></svg>
        <span>www.CorvaneTables.com</span>
      </li>
    </ul>

    <div class="tagline-band"></div>
    <p class="tagline-strip">Wooden Tables &amp; Furniture of the Highest Quality</p>
    <div class="tagline-base"></div>
  </section>

  <section class="card card--back">
    <svg class="card-texture" aria-hidden="true"><rect width="100%" height="100%" filter="url(#paper-grain)"/></svg>

    <p class="brand-name">Corvane Tables</p>
    <p class="brand-tagline">Wooden Tables &amp; Furniture of the Highest Quality</p>
  </section>
</body>
</html>
```